Brimble - ESD in class

We need a flyer to promote our environmental education project to teachers in schools. You have already made the logo and know the style. In the attachment you can find a suggestion how it could be, but the dark background for example is not optimal (and the logo is also an old one).
The following content must be included:
- The title of the project for the flyer is "Education for Sustainable Development (ESD) - Communication of current environmental issues and their connection to society and economy in schools"
- Further, the logo of the project, of the TKR and of the school board should be included (see flyer below right).
- Our offer should stand out clearly, as teachers should see at first glance what we offer: "School visits", "Excursions", "Teacher training"
Each of these offers is described in the flyer, please follow the draft for that content.
- In addition, the topic proposals are also important to appear: "Wild bees", "Green areas", "Virtual water", "Food waste", "(micro) plastic"
- Lastly, the contact should be given, you can find this at the bottom of the flyer: "Karin Vogt, karin.vogt@tkr-example.li, +423 384 17 90"
For the priorities of the contents you can stick to the suggestion in the flyer first.
Look and feel
Each slider illustrates characteristics of the customer's brand and the style your logo design should communicate.

```html
<!DOCTYPE html>
<html lang="en">
<head>
<meta charset="utf-8">
<title>Brimble – ESD in class flyer</title>
<link href="https://fonts.googleapis.com/css2?family=Montserrat:wght@600;700;800;900&family=Poppins:wght@400;500;600&display=swap" rel="stylesheet">
<style>
:root{
  --navy:#101c4e;
  --orange:#f0891b;
  --paper:#f6f5f9;
  --stage:#e4e3e8;
  --ink:#1a1d33;
  --line:#2a2f52;
}
*{box-sizing:border-box;margin:0;padding:0}
html,body{width:1200px;height:800px;overflow:hidden;background:var(--stage)}
body{font-family:"Poppins",sans-serif;color:var(--ink)}
.flyer{position:absolute;left:324px;top:10px;width:552px;height:780px;background:var(--paper);box-shadow:0 6px 24px rgba(0,0,0,.15);overflow:hidden}
.header{background:var(--navy);height:132px;padding:24px 30px 0;text-align:center}
.title{font-family:"Montserrat",sans-serif;font-weight:800;color:var(--orange);font-size:24px;line-height:1.15;letter-spacing:-.2px}
.subtitle{color:#fff;font-size:14px;line-height:1.35;margin-top:10px}
.logos{position:relative;height:78px}
.brand{position:absolute;top:26px;display:flex;align-items:center;gap:8px;font-weight:600;color:var(--navy)}
.brand-dot{width:26px;height:26px;border-radius:50%;background:var(--navy);flex:none}
.brand-name{font-size:17px;line-height:1}
.brand.project{left:30px}
.brand.board{left:50%;transform:translateX(-50%);top:30px}
.brand.board .brand-dot{width:16px;height:18px;border-radius:0}
.brand.board .brand-name{font-size:12px}
.brand.society{right:30px}
.tab{position:absolute;left:50%;transform:translateX(-50%);background:var(--navy);color:var(--orange);font-family:"Montserrat",sans-serif;font-weight:900;padding:7px 26px 5px;border-radius:10px 10px 0 0;white-space:nowrap;z-index:2}
.offer{position:absolute;left:24px;right:24px;top:232px;height:318px;border:1.5px solid var(--line)}
.offer-tab{top:-34px;font-size:21px}
.offer-row{display:flex;height:33.33%;border-top:1.5px dotted var(--line)}
.offer-row:first-child{border-top:none}
.offer-label{width:148px;display:flex;flex-direction:column;align-items:center;justify-content:center;gap:6px;border-right:1.5px dotted var(--line)}
.offer-name{font-family:"Montserrat",sans-serif;font-weight:900;font-size:13px;color:var(--navy);letter-spacing:-.2px}
.offer-text{flex:1;padding:14px 18px;font-size:12px;line-height:1.5;display:flex;flex-direction:column;justify-content:center}
.topics{position:absolute;left:24px;right:24px;top:590px;height:130px;border:1.5px solid var(--line)}
.topics-tab{top:-32px;font-size:19px}
.topic-list{display:flex;justify-content:space-around;padding-top:22px}
.topic{display:flex;flex-direction:column;align-items:center;gap:8px;width:92px}
.topic-icon{width:56px;height:56px;border-radius:50%;background:var(--navy);border:3px solid var(--paper);box-shadow:0 0 0 1.5px var(--navy)}
.topic-name{font-size:12px;font-weight:500;white-space:nowrap}
.footer{position:absolute;left:0;right:0;bottom:0;height:44px;background:var(--navy);color:#fff;display:flex;align-items:center;justify-content:center;gap:26px;font-size:12px}
.contact{display:flex;align-items:center;gap:7px}
.contact-icon{width:16px;height:16px}
</style>
</head>
<body>
<main class="flyer">
  <header class="header">
    <h1 class="title">Education for Sustainable Development (ESD)</h1>
    <p class="subtitle">Communication of current environmental issues and their connection<br>to society and economy in schools</p>
  </header>

  <div class="logos">
    <div class="brand project"><span class="brand-dot"></span><span class="brand-name">Brimble</span></div>
    <div class="brand board"><span class="brand-dot"></span><span class="brand-name">Schulamt Nordtal</span></div>
    <div class="brand society"><span class="brand-dot"></span><span class="brand-name">TKR</span></div>
  </div>

  <section class="offer">
    <h2 class="tab offer-tab">OUR OFFER</h2>
    <div class="offer-row">
      <div class="offer-label">
        <svg width="48" height="44" viewBox="0 0 48 44" fill="none" stroke="#f0891b" stroke-width="2.5" stroke-linejoin="round"><rect x="20" y="4" width="22" height="36"/><path d="M25 11h4M33 11h4M25 18h4M33 18h4M25 25h4M33 25h4"/><path d="M12 40s-9-10-9-16a9 9 0 0 1 18 0c0 6-9 16-9 16z"/><circle cx="12" cy="24" r="3"/></svg>
        <span class="offer-name">SCHOOL VISITS</span>
      </div>
      <div class="offer-text"><p>Expansion of the «nature, people, society» - Teaching through interdisciplinary networking current environmental issues</p><p>Scope: 1-3h</p></div>
    </div>
    <div class="offer-row">
      <div class="offer-label">
        <svg width="52" height="40" viewBox="0 0 52 40" fill="none" stroke="#f0891b" stroke-width="2.5" stroke-linejoin="round"><rect x="14" y="3" width="22" height="6"/><path d="M6 28V18l6-9h30l6 9v10z"/><path d="M14 18h26"/><circle cx="15" cy="30" r="5"/><circle cx="39" cy="30" r="5"/></svg>
        <span class="offer-name">EXCURSIONS</span>
      </div>
      <div class="offer-text"><p>Excursions serve as an extension of the in the School visits theoretically introduced topics.</p><p>Scope: 1-3h</p></div>
    </div>
    <div class="offer-row">
      <div class="offer-label">
        <svg width="46" height="44" viewBox="0 0 46 44" fill="none" stroke="#f0891b" stroke-width="2.5" stroke-linejoin="round"><rect x="6" y="10" width="34" height="24"/><path d="M3 41h40M23 34v7M26 3h12v8"/><circle cx="16" cy="18" r="3"/><path d="M11 29a5 5 0 0 1 10 0M25 18h10M25 24h10"/></svg>
        <span class="offer-name">TEACHER TRAINING</span>
      </div>
      <div class="offer-text"><p>In the case of teacher training, the Elaboration of a topic with special Focus on interdisciplinary links and classification in the three spheres of the environment, Society and economy in the center.</p><p>Length: 4 h</p></div>
    </div>
  </section>

  <section class="topics">
    <h2 class="tab topics-tab">SUGGESTED TOPICS:</h2>
    <div class="topic-list">
      <div class="topic"><div class="topic-icon" role="img" aria-label="Wild bee emblem"></div><span class="topic-name">Wild bees</span></div>
      <div class="topic"><div class="topic-icon" role="img" aria-label="Green areas emblem with trees"></div><span class="topic-name">Green areas</span></div>
      <div class="topic"><svg class="topic-icon" viewBox="0 0 56 56" role="img" aria-label="Water waves"><circle cx="28" cy="28" r="28" fill="#101c4e"/><path d="M14 20q3.5-4 7 0t7 0 7 0 7 0M14 28q3.5-4 7 0t7 0 7 0 7 0M14 36q3.5-4 7 0t7 0 7 0 7 0" fill="none" stroke="#fff" stroke-width="2"/></svg><span class="topic-name">Virtual water</span></div>
      <div class="topic"><div class="topic-icon" role="img" aria-label="Food waste emblem"></div><span class="topic-name">Food waste</span></div>
      <div class="topic"><div class="topic-icon" role="img" aria-label="Micro plastic in water emblem"></div><span class="topic-name">(micro) plastic</span></div>
    </div>
  </section>

  <footer class="footer">
    <span class="contact">Karin Vogt</span>
    <span class="contact"><svg class="contact-icon" viewBox="0 0 16 16"><circle cx="8" cy="8" r="7.5" fill="#f0891b"/><path d="M5 4l2 2-1 1.5q1 2 2.5 2.5L10 9l2 2-1.3 1.2Q7 12 4 6.5z" fill="#101c4e"/></svg>+423 384 17 90</span>
    <span class="contact"><svg class="contact-icon" viewBox="0 0 16 16"><circle cx="8" cy="8" r="7.5" fill="#f0891b"/><rect x="4" y="5" width="8" height="6" fill="none" stroke="#101c4e" stroke-width="1.2"/><path d="M4 5l4 3.5L12 5" fill="none" stroke="#101c4e" stroke-width="1.2"/></svg>karin.vogt@tkr-example.li</span>
  </footer>
</main>
</body>
</html>
```